Company website design for Brindlemoor Valuation Advisory LLC

Design of company website. See uploaded outline. Logo hex codes for the icon colors: middle blue - 4D6C8A, dark blue - 11122B.

```html
<!DOCTYPE html>
<html lang="en">
<head>
<meta charset="utf-8">
<title>Brindlemoor Valuation Advisory LLC</title>
<link href="https://fonts.googleapis.com/css2?family=Montserrat:wght@300;400;500;600;700;800&family=Roboto:wght@300;400;500&display=swap" rel="stylesheet">
<style>
:root{
  --navy:#11122B;
  --blue:#4D6C8A;
  --band:#52718F;
  --band-light:#5B7998;
  --tile:#5D7B9A;
  --ink:#1c2233;
  --muted:#5a6170;
  --white:#ffffff;
  --faint:#eef1f4;
}
*{margin:0;padding:0;box-sizing:border-box}
html,body{width:1200px;height:3567px;overflow:hidden}
body{position:relative;background:var(--white);font-family:'Roboto',sans-serif;color:var(--ink)}
.abs{position:absolute}
.mont{font-family:'Montserrat',sans-serif}

/* header */
.site-header{position:absolute;left:0;top:0;width:1200px;height:79px;background:var(--white)}
.brand{position:absolute;display:flex;align-items:center;gap:10px}
.brand-square{background:var(--blue)}
.brand-text{font-family:'Montserrat',sans-serif;font-weight:500;color:var(--navy);line-height:1}
.menu-btn{position:absolute;left:1002px;top:17px;width:98px;height:41px;background:#f2f3f5;border-radius:3px;display:flex;align-items:center;justify-content:center;gap:8px;font:500 14px 'Montserrat',sans-serif;color:var(--navy)}

/* hero */
.hero{position:absolute;left:0;top:79px;width:1200px;height:624px;background:linear-gradient(180deg,#c9ccce 0%,#a7a49d 22%,#8d8478 38%,#6b6a64 52%,#3a4439 70%,#26302a 100%)}
.hero-text{position:absolute;left:0;width:1200px;text-align:center;color:var(--white)}
.hero-l1{top:388px;font:300 56px/1 'Montserrat',sans-serif;letter-spacing:1px}
.hero-l2{top:446px;font:700 58px/1 'Montserrat',sans-serif}
.hero-sub{top:518px;font:400 28px/1 'Roboto',sans-serif}

/* values */
.values{position:absolute;left:0;top:703px;width:1200px;height:212px;background:var(--band)}
.values h2{position:absolute;top:53px;width:1200px;text-align:center;font:300 38px 'Montserrat',sans-serif;color:var(--white)}
.values h2 b{font-weight:700}
.value{position:absolute;top:127px;font:600 19px 'Montserrat',sans-serif;color:var(--white)}
.value-sep{position:absolute;top:121px;width:1px;height:34px;background:rgba(255,255,255,.25)}

/* section titles */
.sec-title{position:absolute;font-family:'Montserrat',sans-serif;line-height:1.05}
.sec-title .t1{display:block;font-weight:300}
.sec-title .t2{display:block;font-weight:700;text-align:right}
.ghost{position:absolute;font:800 74px 'Montserrat',sans-serif;letter-spacing:2px;white-space:nowrap}
.big-num{position:absolute;font:800 128px/1 'Montserrat',sans-serif}

/* services */
.service{position:absolute;width:300px}
.service h3{font:700 16px/1.3 'Montserrat',sans-serif;color:var(--ink)}
.service p{font:400 11.5px/1.75 'Roboto',sans-serif;color:var(--muted);margin-top:4px}
.service-icon{position:absolute;width:56px;height:56px}

/* who we serve */
.serve{position:absolute;left:0;top:1391px;width:1200px;height:563px;background:var(--band)}
.diamond{position:absolute;width:186px;height:186px;background:var(--tile);transform:rotate(45deg)}
.serve-item{position:absolute;width:200px;text-align:center;color:var(--white);font:500 16px/1.25 'Montserrat',sans-serif}
.serve-item svg{display:block;margin:0 auto 8px}

/* industries */
.tile{position:absolute;width:236px;height:215px}
.tile span{position:absolute;left:0;bottom:14px;width:100%;text-align:center;color:var(--white);font:600 17px/1.05 'Montserrat',sans-serif}

/* contact */
.contact{position:absolute;left:0;top:2605px;width:1200px;height:584px;background:var(--band)}
.label{position:absolute;font:600 13px 'Montserrat',sans-serif;color:var(--white)}
.field{position:absolute;border:1px solid rgba(255,255,255,.6);padding:0 15px;font:400 14px 'Roboto',sans-serif;color:var(--white);display:flex;align-items:center}
.field.area{align-items:flex-start;padding-top:14px}
.check{position:absolute;left:397px;top:3064px;width:191px;height:49px;background:#f9f9f9;border:1px solid #d3d3d3;display:flex;align-items:center;gap:8px;padding-left:10px;font:400 10px 'Roboto',sans-serif;color:#222}
.check i{display:block;width:16px;height:16px;border:2px solid #c1c1c1;background:#fff}
.submit{position:absolute;left:605px;top:3064px;width:181px;height:49px;background:var(--white);color:var(--blue);font:500 16px 'Roboto',sans-serif;display:flex;align-items:center;justify-content:center}

/* footer */
.foot-head{position:absolute;top:3262px;font:500 22px 'Montserrat',sans-serif;color:var(--ink)}
.foot-list{position:absolute;top:3306px;list-style:none;font:400 15px 'Roboto',sans-serif;color:var(--ink)}
.foot-list li{height:32px}
.foot-contact{position:absolute;left:464px;display:flex;gap:14px;align-items:flex-start;font:400 16px/1.4 'Roboto',sans-serif;color:var(--ink)}
.foot-contact .ic{width:34px;height:34px;border-radius:50%;background:#eef1f5;display:flex;align-items:center;justify-content:center;flex:none;margin-top:-4px}
.social{position:absolute;top:3367px;width:40px;height:40px;border-radius:50%;background:var(--ink)}
.rule{position:absolute;left:100px;top:3506px;width:1000px;height:1px;background:#c9ccd2}
.copy{position:absolute;top:3526px;width:1200px;text-align:center;font:400 13px 'Roboto',sans-serif;color:var(--ink)}
</style>
</head>
<body>

<header class="site-header">
  <div class="brand" style="left:100px;top:14px">
    <div class="brand-square" style="width:50px;height:50px"></div>
    <div class="brand-text"><div style="font-size:30px">BRINDLEMOOR</div><div style="font-size:13px;letter-spacing:1.6px;margin-top:4px">VALUATION ADVISORY LLC</div></div>
  </div>
  <div class="menu-btn">MENU
    <svg width="30" height="18" viewBox="0 0 30 18"><g stroke="#11122B" stroke-width="1.6"><line x1="0" y1="2" x2="30" y2="2"/><line x1="0" y1="9" x2="24" y2="9"/><line x1="0" y1="16" x2="18" y2="16"/></g></svg>
  </div>
</header>

<section class="hero" role="img" aria-label="Jagged granite mountain peaks with snow patches above a dark pine forest under a grey sky">
  <div class="hero-text hero-l1">BUILDING A BUSINESS</div>
  <div class="hero-text hero-l2">IS A JOURNEY</div>
  <div class="hero-text hero-sub">We have the valuation expertise to guide you</div>
</section>

<section class="values">
  <h2>Our <b>Values</b></h2>
  <div class="value" style="left:102px">INTEGRITY</div>
  <div class="value-sep" style="left:245px"></div>
  <div class="value" style="left:280px">RESPONSIVENESS</div>
  <div class="value-sep" style="left:498px"></div>
  <div class="value" style="left:534px">EXCELLENCE</div>
  <div class="value-sep" style="left:700px"></div>
  <div class="value" style="left:735px">RELATIONSHIPS</div>
  <div class="value-sep" style="left:934px"></div>
  <div class="value" style="left:969px">COMMUNITY</div>
</section>

<!-- what we do -->
<div class="ghost" style="left:96px;top:965px;color:transparent;-webkit-text-stroke:1px #eef0f3">OUR SERVICES</div>
<div class="sec-title" style="left:100px;top:1036px;width:210px;font-size:38px;color:var(--blue)"><span class="t1">What We</span><span class="t2">Do</span></div>
<div class="big-num" style="left:106px;top:1190px;color:var(--faint)">02</div>

<svg width="0" height="0" style="position:absolute">
  <defs>
    <symbol id="tax-doc" viewBox="0 0 56 56">
      <g fill="none" stroke="#2b3448" stroke-width="1.6">
        <path d="M4 2h30l8 8v34H4z"/><path d="M34 2v8h8"/>
        <line x1="9" y1="22" x2="37" y2="22"/><line x1="9" y1="27" x2="37" y2="27"/><line x1="9" y1="32" x2="30" y2="32"/><line x1="9" y1="37" x2="26" y2="37"/>
        <circle cx="43" cy="43" r="10" fill="#fff"/><path d="M38 43l4 4 7-8"/>
      </g>
      <text x="9" y="16" font-family="Montserrat,sans-serif" font-size="10" font-weight="600" fill="#2b3448">TAX</text>
    </symbol>
  </defs>
</svg>

<svg class="service-icon" style="left:362px;top:1030px"><use href="#tax-doc"/></svg>
<div class="service" style="left:430px;top:1030px"><h3>TAX-RELATED VALUATIONS</h3><p>Valuations for estate/gift tax, charitable contributions, equity-linked compensation, corporate restructuring and insolvency purposes.</p></div>
<svg class="service-icon" style="left:739px;top:1030px"><use href="#tax-doc"/></svg>
<div class="service" style="left:804px;top:1030px"><h3>FINANCIAL REPORTING</h3><p>Our work includes purchase price allocations, fresh-start accounting, impairment analyses, equity-linked compensation, leases and financial instruments.</p></div>
<svg class="service-icon" style="left:362px;top:1158px"><use href="#tax-doc"/></svg>
<div class="service" style="left:430px;top:1158px"><h3>FINANCING &amp; TRANSACTION ADVISORY</h3><p>Financial assessments to evaluate debt structure &amp;capital adequacy. Valuation support for loan underwriting, capital raises, share redemptions, minority interest buyouts, buy-sell agreements as well as for mergers, acquisitions and divestitures.</p></div>
<svg class="service-icon" style="left:739px;top:1158px"><use href="#tax-doc"/></svg>
<div class="service" style="left:804px;top:1158px"><h3>BUSINESS PLANNING &amp; ADVISORY</h3><p>Outsourced financial planning and analysis (FP&amp;A) services, including model development, strategy valuation and exit options analysis.</p></div>

<!-- who we serve -->
<section class="serve">
  <div class="ghost" style="left:86px;top:40px;color:transparent;-webkit-text-stroke:1px rgba(255,255,255,.12)">FOCUS AREA</div>
  <div class="sec-title" style="left:103px;top:85px;width:268px;font-size:38px;color:var(--white)"><span class="t1">Who Do</span><span class="t2">We Serve</span></div>
  <div class="big-num" style="left:106px;top:322px;color:rgba(255,255,255,.12)">03</div>

  <div class="diamond" style="left:455px;top:131px"></div>
  <div class="diamond" style="left:733px;top:138px"></div>
  <div class="diamond" style="left:593px;top:271px"></div>
  <div class="diamond" style="left:870px;top:276px"></div>

  <div class="serve-item" style="left:448px;top:158px">
    <svg width="92" height="84" viewBox="0 0 92 84" fill="none" stroke="#fff" stroke-width="2.2"><circle cx="28" cy="18" r="12"/><circle cx="64" cy="18" r="12"/><path d="M6 80V56c0-10 10-18 22-18s22 8 22 18"/><path d="M42 56c0-10 10-18 22-18s22 8 22 18v24"/><circle cx="46" cy="50" r="9"/><path d="M32 80c0-9 6-15 14-15s14 6 14 15"/></svg>
    Family-Owned<br>Businesses
  </div>
  <div class="serve-item" style="left:726px;top:174px">
    <svg width="70" height="72" viewBox="0 0 70 72" fill="none" stroke="#fff" stroke-width="2.2"><rect x="6" y="48" width="8" height="20"/><rect x="20" y="38" width="8" height="30"/><rect x="34" y="44" width="8" height="24"/><rect x="48" y="30" width="8" height="38"/><polyline points="8,28 24,16 38,22 56,6"/><circle cx="8" cy="28" r="3"/><circle cx="24" cy="16" r="3"/><circle cx="38" cy="22" r="3"/><circle cx="58" cy="5" r="3"/></svg>
    Publicly Traded<br>Companies
  </div>
  <div class="serve-item" style="left:586px;top:296px">
    <svg width="58" height="58" viewBox="0 0 58 58" fill="none" stroke="#fff" stroke-width="2.2"><circle cx="29" cy="29" r="26"/><path d="M36 20c-2-3-5-4-8-4-4 0-7 2-7 6 0 8 15 5 15 13 0 4-3 6-8 6-3 0-6-1-8-4M29 12v34"/></svg>
    Private-Equity<br>Sponsored<br>Companies
  </div>
  <div class="serve-item" style="left:863px;top:311px">
    <svg width="76" height="72" viewBox="0 0 76 72" fill="none" stroke="#fff" stroke-width="2.2"><path d="M4 18L34 4l30 14z"/><line x1="4" y1="22" x2="64" y2="22"/><line x1="10" y1="26" x2="10" y2="56"/><line x1="58" y1="26" x2="58" y2="40"/><rect x="20" y="28" width="28" height="24"/><text x="29" y="46" font-family="Montserrat,sans-serif" font-size="16" fill="#fff" stroke="none">$</text><line x1="2" y1="60" x2="50" y2="60"/><rect x="52" y="44" width="20" height="8"/><rect x="52" y="52" width="20" height="8"/><rect x="52" y="60" width="20" height="8"/></svg>
    Lenders
  </div>
</section>

<!-- industries -->
<div class="ghost" style="left:96px;top:2005px;color:transparent;-webkit-text-stroke:1px #eef0f3">INDUSTRIES</div>
<div class="sec-title" style="left:100px;top:2076px;width:235px;font-size:38px;color:var(--blue)"><span class="t1">Industries</span><span class="t2">Served</span></div>
<div class="big-num" style="left:102px;top:2380px;color:var(--faint)">04</div>

<div class="tile" style="left:360px;top:2065px;background:linear-gradient(135deg,#5a5048,#2c2a2c 55%,#1f3a48)" role="img" aria-label="Person working at a holographic technology display"><span>Technology</span></div>
<div class="tile" style="left:612px;top:2065px;background:linear-gradient(160deg,#8e8f90,#b37a2e 45%,#6c6c6e)" role="img" aria-label="Orange industrial robot arms on an assembly line"><span>Manufacturing</span></div>
<div class="tile" style="left:864px;top:2065px;background:linear-gradient(150deg,#a99c88,#7d7872 50%,#5d5d60)" role="img" aria-label="Warehouse workers handling boxes on a conveyor"><span>Wholesale / Distribution</span></div>
<div class="tile" style="left:360px;top:2296px;background:linear-gradient(160deg,#b9bdc2,#6d6e72 50%,#3c3d44)" role="img" aria-label="Business team meeting around a table"><span style="bottom:18px">Business &amp; Professional<br>Services</span></div>
<div class="tile" style="left:612px;top:2296px;background:linear-gradient(150deg,#d6d1cc,#c67a70 45%,#5a5560)" role="img" aria-label="Shopper browsing laptops in an electronics store"><span>Retail</span></div>
<div class="tile" style="left:864px;top:2296px;background:linear-gradient(150deg,#8d8780,#b39370 50%,#6e5c4a)" role="img" aria-label="Person checking a phone among stacked parcels"><span>Consumer Products</span></div>

<!-- contact -->
<section class="contact">
  <div class="ghost" style="left:108px;top:40px;color:transparent;-webkit-text-stroke:1px rgba(255,255,255,.12)">GET IN TOUCH</div>
  <div class="sec-title" style="left:115px;top:85px;width:174px;font-size:38px;color:var(--white)"><span class="t1">Contact</span><span class="t2">Us</span></div>
  <div class="big-num" style="left:126px;top:340px;color:rgba(255,255,255,.12)">05</div>
</section>
<div class="label" style="left:396px;top:2683px">First Name*</div>
<div class="field" style="left:396px;top:2710px;width:313px;height:44px">Your Name</div>
<div class="label" style="left:731px;top:2683px">Email Address*</div>
<div class="field" style="left:731px;top:2710px;width:313px;height:44px">email@yourmail.com</div>
<div class="label" style="left:396px;top:2790px">Subject*</div>
<div class="field" style="left:396px;top:2817px;width:649px;height:43px">Subject</div>
<div class="label" style="left:396px;top:2891px">Comments / Questions*</div>
<div class="field area" style="left:396px;top:2917px;width:649px;height:126px">Your Message</div>
<div class="check"><i></i>I'm not a robot<span style="margin-left:auto;margin-right:10px;width:22px;height:22px;background:#c9d3e0"></span></div>
<div class="submit">SUBMIT MESSAGE</div>

<!-- footer -->
<div class="foot-head" style="left:101px">Quick Links</div>
<ul class="foot-list" style="left:101px"><li>Home</li><li>Our Values</li><li>What We Do</li><li>Who Do We Serve</li><li>Industries Served</li><li>Contact Us</li></ul>
<div class="foot-head" style="left:281px">Other Links</div>
<ul class="foot-list" style="left:281px"><li>Privacy Policy</li><li>Terms of Service</li><li>Credit</li><li>FAQ</li></ul>
<div class="foot-head" style="left:464px">Contact Us</div>
<div class="foot-contact" style="top:3308px"><span class="ic"><svg width="14" height="18" viewBox="0 0 14 18"><path d="M7 1a6 6 0 0 0-6 6c0 5 6 10 6 10s6-5 6-10a6 6 0 0 0-6-6z" fill="none" stroke="#4D6C8A" stroke-width="1.8"/><circle cx="7" cy="7" r="2" fill="#4D6C8A"/></svg></span><div>1480 W Larkspur Ridge Rd<br>Suite 210, Aldenbrook, ID 83999</div></div>
<div class="foot-contact" style="top:3375px"><span class="ic"><svg width="16" height="16" viewBox="0 0 16 16"><path d="M3 1l3 3-2 2c1 3 3 5 6 6l2-2 3 3-2 2C7 15 1 9 1 3z" fill="none" stroke="#4D6C8A" stroke-width="1.6"/></svg></span><div>+1 555 014 2290</div></div>
<div class="foot-contact" style="top:3438px"><span class="ic"><svg width="16" height="12" viewBox="0 0 16 12"><rect x="1" y="1" width="14" height="10" fill="none" stroke="#4D6C8A" stroke-width="1.5"/><path d="M1 1l7 6 7-6" fill="none" stroke="#4D6C8A" stroke-width="1.5"/></svg></span><div>info@brindlemoorvaluation.com</div></div>

<div class="brand" style="left:760px;top:3264px">
  <div class="brand-square" style="width:66px;height:66px"></div>
  <div class="brand-text"><div style="font-size:40px">BRINDLEMOOR</div><div style="font-size:16px;letter-spacing:2.2px;margin-top:6px">VALUATION ADVISORY LLC</div></div>
</div>
<div class="social" style="left:769px" aria-label="Social profile 1"></div>
<div class="social" style="left:816px" aria-label="Social profile 2"></div>
<div class="social" style="left:863px" aria-label="Social profile 3"></div>
<div class="social" style="left:910px" aria-label="Social profile 4"></div>

<div class="rule"></div>
<div class="copy">Copyright © 2022 Brindlemoor. All rights reserved.</div>

</body>
</html>
```